Standardization and redesign of graphics for a non-fiction book

For a book project, 11 graphics need to be visually unified so that all the graphics in the book are in the same style. The graphics must be created from scratch. Just new colors aren't enough. Some of the existing graphics are by other authors who own the copyright. Accordingly, the new graphics must be truly new. This is especially true for the "2 S-curves" graphic.

Target Market(s)

Manager Furniture Industry

Industry/Entity Type

Möbel

Colors
0054AA
0677BA
7BADD7
CADEEF
E8F1F8

```html
<!DOCTYPE html>
<html lang="en">
<head>
<meta charset="utf-8">
<title>Customer Journey</title>
<link rel="stylesheet" href="https://fonts.googleapis.com/css2?family=Source+Sans+3:wght@700;900&family=Fira+Sans:wght@700&display=swap">
<style>
  :root {
    --page: #ffffff;
    --panel: #f3fafd;
    --edge: #4a4a4a;
    --ink: #111111;
    --icon-line: #1748f0;
    --icon-fill: #c4ebfb;
  }
  * { margin: 0; padding: 0; box-sizing: border-box; }
  html, body {
    width: 1200px; height: 545px; overflow: hidden;
    background: var(--page);
  }
  .canvas { position: relative; width: 1200px; height: 545px; }
  .journey-panel {
    position: absolute; left: 47px; top: 44px; width: 1110px; height: 458px;
    background: var(--panel);
    border-right: 3px solid var(--edge);
    border-bottom: 3px solid var(--edge);
    box-shadow: 6px 8px 14px rgba(0,0,0,0.18);
  }
  .journey-title {
    position: absolute; left: 0; right: 0; top: 104px;
    text-align: center;
    font-family: "Source Sans 3", sans-serif;
    font-weight: 900; font-size: 40px; letter-spacing: 1px;
    color: var(--ink);
  }
  .stage {
    position: absolute; top: 228px; width: 180px; margin-left: -90px;
    text-align: center;
  }
  .stage-icon { display: block; width: 80px; height: 76px; margin: 0 auto; }
  .stage-icon * { stroke: var(--icon-line); stroke-width: 4; stroke-linejoin: round; stroke-linecap: round; }
  .stage-icon .fill { fill: var(--icon-fill); }
  .stage-icon .solid { fill: var(--icon-line); stroke: none; }
  .stage-icon .none { fill: none; }
  .stage-label {
    margin-top: 18px;
    font-family: "Fira Sans", sans-serif;
    font-weight: 700; font-size: 20px; letter-spacing: 0.3px;
    color: var(--ink);
  }
</style>
</head>
<body>
<div class="canvas">
  <div class="journey-panel">
    <h1 class="journey-title">CUSTOMER JOUNRNEY</h1>

    <div class="stage" style="left:114px">
      <svg class="stage-icon" viewBox="0 0 80 76" aria-hidden="true">
        <circle class="none" cx="40" cy="33" r="31"/>
        <circle class="none" cx="40" cy="33" r="26"/>
        <path class="fill" d="M31 53 C26 44 20 40 20 31 A20 20 0 0 1 60 31 C60 40 54 44 49 53 Z"/>
        <rect class="fill" x="31" y="53" width="18" height="6"/>
        <path class="fill" d="M32 59 H48 A8 8 0 0 1 32 59 Z"/>
      </svg>
      <p class="stage-label">Awareness</p>
    </div>

    <div class="stage" style="left:347px">
      <svg class="stage-icon" viewBox="0 0 80 76" aria-hidden="true">
        <path class="fill" d="M14 6 H72 V74 H20 A6 6 0 0 1 14 68 Z"/>
        <line x1="20" y1="6" x2="20" y2="62"/>
        <path class="none" d="M72 62 H20 A6 6 0 0 0 20 74"/>
        <line x1="28" y1="68" x2="64" y2="68"/>
        <circle class="none" cx="48" cy="27" r="10"/>
        <circle class="none" cx="48" cy="27" r="6" style="stroke-width:2"/>
        <line x1="55" y1="34" x2="63" y2="42" style="stroke-width:7"/>
      </svg>
      <p class="stage-label">Consideration</p>
    </div>

    <div class="stage" style="left:576px">
      <svg class="stage-icon" viewBox="0 0 80 76" aria-hidden="true">
        <path class="fill" d="M12 24 L21 6 H59 L68 24 Z"/>
        <rect class="fill" x="15" y="24" width="50" height="50"/>
        <line x1="8" y1="74" x2="72" y2="74"/>
        <rect class="solid" x="22" y="35" width="10" height="8"/>
        <rect class="solid" x="35" y="35" width="10" height="8"/>
        <rect class="solid" x="48" y="35" width="10" height="8"/>
        <rect class="solid" x="22" y="51" width="10" height="8"/>
        <rect class="solid" x="48" y="51" width="10" height="8"/>
        <rect class="solid" x="35" y="51" width="10" height="23"/>
      </svg>
      <p class="stage-label">Retention</p>
    </div>

    <div class="stage" style="left:780px">
      <svg class="stage-icon" viewBox="0 0 80 76" aria-hidden="true">
        <path class="none" d="M27 29 V16 A13 13 0 0 1 53 16 V29"/>
        <path class="fill" d="M12 24 H64 L66 70 H10 Z"/>
        <circle class="fill" cx="60" cy="57" r="17"/>
        <path class="none" d="M52 57 L58 63 L67 50" style="stroke-width:5"/>
      </svg>
      <p class="stage-label">Purchase</p>
    </div>

    <div class="stage" style="left:991px">
      <svg class="stage-icon" viewBox="0 0 100 76" aria-hidden="true">
        <path class="fill" d="M38 3 H97 L87 73 H28 Z"/>
        <line x1="20" y1="28" x2="45" y2="28"/>
        <line x1="11" y1="37" x2="45" y2="37"/>
        <line x1="2" y1="46" x2="45" y2="46"/>
        <circle class="fill" cx="64" cy="37" r="17"/>
        <line x1="55" y1="46" x2="71" y2="30"/>
        <circle class="none" cx="54" cy="47" r="3" style="stroke-width:2.5"/>
        <path class="none" d="M70 26 A5 5 0 0 0 76 33" style="stroke-width:3"/>
      </svg>
      <p class="stage-label">Loallty</p>
    </div>
  </div>
</div>
</body>
</html>
```